A Team Treasury Hunt Across Melbourne Landmark

I require a poster design to promote an 'Tolvane Quest' style event in Melbourne, Australia. Teams will have to navigate, solve clues and complete activities in a race across the city.

I would like a poster with the event name 'Velmorand' in large 'Circus' font arced across the bottom third of the design.
I would like the event to have the tag line 'Good Friends. Better Rivals.' I don't have a preference on the style, but wish it to be dramatic and portray heated competition.

The event is being held in Melbourne, so I wish for the design to prominently feature a Melbourne landmark. I have attached a number of pictures taken in Melbourne. It may be advisable to only feature one landmark. Harrowby Lane Station is probably the most recognisable landmark.

I don't wish for the design to be overly cluttered. I would like a design that clearly communicated competition. Some ideas may be a finishing line or a starting pistol. But please don't be limited by these suggestions.

I'm one for the dramatic, so prefer designs to be slightly darker and dramatic.
Updates

Project Deadline Extended Reason: Whilst I'm grateful to those who have taken the time and effort to submit a design, they are not what I'm looking for. As a result, I have updated my brief, trying to make it a lot clear what I'm looking for. I have also increased the budget to attract more designs. I have extended the deadline to give new designers the opportunity to submit designs. Added Thursday, May 28, 2015

Target Market(s)

To promote a birthday event which will be attended by friends.

Industry/Entity Type

Event

Font styles to use
Other font styles liked:
• Circus

Requirements
Must have
• The event name 'Velmorand' in large 'Circus' font arced across the bottom third of the design.
• The tag line 'Good Friends. Better Rivals.' I don't have a preference on the style, but wish it to be dramatic and portray heated competition.
• The design should prominently feature a Melbourne landmark.
• Slightly dark and dramatic.
Nice to have
• A design which looks dramatic and striking, creating intrigue.
Should not have
• N/A

```html
<!DOCTYPE html>
<html lang="en">
<head>
<meta charset="utf-8">
<title>Velmorand – Event Posters</title>
<link rel="stylesheet" href="https://fonts.googleapis.com/css2?family=Poppins:wght@700&family=Montserrat:wght@500&family=Rye&display=swap">
<style>
  :root {
    --page: #ffffff;
    --gold: #f2c27a;
    --maroon: #7a2a2c;
    --maroon-dark: #4e1718;
    --band: #050505;
    --white: #ffffff;
  }
  html, body {
    margin: 0;
    padding: 0;
    width: 1200px;
    height: 1000px;
    overflow: hidden;
    background: var(--page);
  }
  .poster {
    position: absolute;
    top: 122px;
    height: 754px;
    overflow: hidden;
    background: var(--band);
  }
  .poster--station { left: 44px; width: 533px; }
  .poster--skyline { left: 628px; width: 517px; }

  .backdrop {
    position: absolute;
    inset: 0 0 auto 0;
    height: 536px;
  }
  .poster--station .backdrop {
    background: linear-gradient(200deg, #d9d9d9 0%, #8c8c8c 30%, #3b3b3b 55%, #9a9a9a 80%, #cfcfcf 100%);
  }
  .poster--skyline .backdrop {
    background:
      radial-gradient(ellipse 60% 30% at 60% 60%, rgba(255,210,140,.45), transparent 70%),
      linear-gradient(180deg, #2b1d17 0%, #4a3424 40%, #6b4b2e 62%, #1f1812 78%, #3a2d24 100%);
  }
  .lower-fill {
    position: absolute;
    left: 0; right: 0; top: 582px; bottom: 0;
  }
  .poster--station .lower-fill {
    background: linear-gradient(180deg, #3a3a3a 0%, #141414 60%, #000 100%);
  }
  .poster--skyline .lower-fill {
    background: linear-gradient(180deg, #3a2c22 0%, #1e1611 60%, #0c0907 100%);
  }

  .tagline {
    position: absolute;
    top: 26px;
    left: 0; right: 0;
    margin: 0;
    text-align: center;
    font-family: "Poppins", sans-serif;
    font-weight: 700;
    font-size: 96px;
    line-height: 95px;
    letter-spacing: 0;
    text-transform: uppercase;
    color: var(--gold);
    text-shadow:
      0 0 6px rgba(255,240,200,.8),
      1px 1px 0 var(--maroon), 2px 2px 0 var(--maroon), 3px 3px 0 var(--maroon),
      4px 4px 0 var(--maroon), 5px 5px 0 var(--maroon), 6px 6px 0 var(--maroon),
      7px 7px 0 var(--maroon), 8px 8px 0 var(--maroon), 9px 9px 0 var(--maroon),
      10px 10px 0 var(--maroon), 11px 11px 0 var(--maroon-dark),
      12px 12px 0 var(--maroon-dark), 14px 14px 10px rgba(0,0,0,.5);
  }
  .tagline span { display: block; }

  .location-band {
    position: absolute;
    left: 0; right: 0;
    top: 536px;
    height: 46px;
    background: var(--band);
    color: var(--white);
    font-family: "Montserrat", sans-serif;
    font-weight: 500;
    font-size: 24px;
    line-height: 46px;
    letter-spacing: 7.2px;
    text-align: right;
    padding-right: 20px;
    box-sizing: border-box;
    white-space: nowrap;
  }

  .event-name {
    position: absolute;
    left: 0; right: 0;
    top: 612px;
    margin: 0;
    text-align: center;
    font-family: "Rye", serif;
    font-weight: 400;
    font-size: 64px;
    line-height: 90px;
    letter-spacing: 0;
    white-space: nowrap;
    color: var(--white);
    transform: scaleY(1.3);
    text-shadow: 0 0 10px rgba(255,255,255,.6), 0 0 2px #fff;
  }
</style>
</head>
<body>

<section class="poster poster--station">
  <div class="backdrop" role="img" aria-label="Black and white photograph of Harrowby Lane Station facade with platform signs and clocks, with a runner silhouette breaking the finish tape"></div>
  <div class="lower-fill" role="img" aria-label="Darkened lower part of the station photograph"></div>
  <h1 class="tagline"><span>Good</span><span>Friends.</span><span>Better</span><span>Rivals.</span></h1>
  <div class="location-band">MELBOURNE, AUSTRALIA</div>
  <p class="event-name">VELMORAND</p>
</section>

<section class="poster poster--skyline">
  <div class="backdrop" role="img" aria-label="Blurred night photograph of the Melbourne skyline over the river, with a runner silhouette breaking the finish tape"></div>
  <div class="lower-fill" role="img" aria-label="Dark river reflections of the city lights"></div>
  <h1 class="tagline"><span>Good</span><span>Friends.</span><span>Better</span><span>Rivals.</span></h1>
  <div class="location-band">MELBOURNE, AUSTRALIA</div>
  <p class="event-name">VELMORAND</p>
</section>

</body>
</html>
```